Medical Equipment Provider Postcard

We are a full service Durable Medical Equipment provider, ORVAN Medical Equipment. We specialize in home medical equipment like oxygen, CPAP/BiPAP, hospital beds, etc. We are a locallly owned and operated business which is important to our small community her in Missouri. We want a high quality, bright, informative postcard that we can hand out to our referral sources (nurses and physicians). I'm attaching our current tri-fold design, we want something more professional and eye-catching.

Industry/Entity Type

Medical

Requirements
Must have
• Our logo
Nice to have
• Our colors are bright blue, black and white but would love to see some eye-catching design ideas!

```html
<!DOCTYPE html>
<html lang="en">
<head>
<meta charset="utf-8">
<title>ORVAN Medical Equipment – Postcard</title>
<link rel="stylesheet" href="https://fonts.googleapis.com/css2?family=Arimo:ital,wght@0,400;0,700;1,700&family=Roboto+Condensed:wght@400;700&display=swap">
<style>
  :root {
    --brand-blue: #0b6db6;
    --accent-blue: #1976bd;
    --heading-blue: #0c6fb8;
    --ink: #1c1c1c;
    --paper: #ffffff;
    --photo-light: #eef1f3;
    --photo-mid: #cfd6dc;
    --divider: #555555;
  }
  * { margin: 0; padding: 0; box-sizing: border-box; }
  html, body { width: 1200px; height: 924px; overflow: hidden; background: var(--paper); }
  .postcard {
    position: relative;
    width: 1200px;
    height: 924px;
    background: var(--paper);
    color: var(--ink);
    font-family: "Arimo", Arial, sans-serif;
  }
  .intro {
    position: absolute;
    left: 48px; top: 42px; width: 1120px;
    font-size: 22.5px; line-height: 34px;
  }
  .intro strong { font-weight: 700; }
  .feature-band { position: absolute; left: 0; top: 175px; width: 1200px; height: 386px; }
  .features {
    position: absolute; left: 44px; top: 218px; width: 620px;
    list-style: none; color: var(--paper);
  }
  .features li {
    position: relative; padding-left: 26px;
    font-weight: 700; font-style: italic;
    font-size: 30px; line-height: 32px;
    margin-bottom: 33px;
  }
  .features li::before {
    content: ""; position: absolute; left: 0; top: 8px;
    border-left: 11px solid #4fb0ee;
    border-top: 8px solid transparent; border-bottom: 8px solid transparent;
  }
  .cta {
    position: absolute; left: 48px; top: 601px;
    color: var(--accent-blue);
    font-weight: 700; font-style: italic;
    font-size: 33px; line-height: 40px;
  }
  .van-photo { position: absolute; left: 815px; top: 578px; width: 360px; height: 225px; }
  .service-note {
    position: absolute; left: 60px; top: 706px;
    font-family: "Roboto Condensed", "Arial Narrow", sans-serif;
    font-size: 22px;
  }
  .location {
    position: absolute; top: 752px;
    font-family: "Roboto Condensed", "Arial Narrow", sans-serif;
  }
  .location--first { left: 54px; }
  .location--second { left: 645px; }
  .location h2 {
    font-family: "Arimo", Arial, sans-serif;
    color: var(--heading-blue);
    font-size: 22px; font-weight: 700; letter-spacing: 0.5px;
    line-height: 30px;
  }
  .location .address, .location .phones { font-size: 23.5px; line-height: 30px; }
  .location .phones b { font-weight: 700; }
  .location .phones .gap { display: inline-block; width: 12px; }
  .location .landmark { font-size: 18px; line-height: 30px; margin-top: 3px; }
  .divider {
    position: absolute; left: 615px; top: 757px;
    width: 1px; height: 128px; background: var(--divider);
  }
</style>
</head>
<body>
<main class="postcard">
  <p class="intro"><strong>ORVAN Medical Equipment</strong> employs RN’s and Respiratory Therapists to assist your physician in getting you the appropriate medical equipment for your specific needs.&nbsp; We have 2 conveniently located showrooms to serve all of Southeast Missouri.</p>

  <svg class="feature-band" viewBox="0 0 1200 386" aria-hidden="false">
    <defs>
      <linearGradient id="clinicTone" x1="0" y1="0" x2="1" y2="1">
        <stop offset="0" stop-color="#f4f6f8"/>
        <stop offset="0.55" stop-color="#dfe5ea"/>
        <stop offset="1" stop-color="#c7d0d8"/>
      </linearGradient>
    </defs>
    <rect x="630" y="0" width="570" height="386" fill="url(#clinicTone)" role="img" aria-label="Photo of a smiling nurse in a white coat assisting an elderly patient in a wheelchair"/>
    <polygon points="0,0 730,0 636,386 0,386" fill="var(--brand-blue)"/>
  </svg>

  <ul class="features">
    <li>We deliver most Durable Medical Equipment free of charge, directly to your home.</li>
    <li>We accept MOST insurances as well as Medicare and Medicaid.</li>
    <li>ORVAN Medical Equipment has 24/7 Emergency on call services</li>
  </ul>

  <h1 class="cta">CALL US TODAY OR STOP BY ONE<br>OF OUR LARGE SHOWROOMS!</h1>

  <svg class="van-photo" viewBox="0 0 360 225">
    <defs>
      <linearGradient id="vanTone" x1="0" y1="0" x2="0" y2="1">
        <stop offset="0" stop-color="#fafbfc"/>
        <stop offset="1" stop-color="#d9dde1"/>
      </linearGradient>
    </defs>
    <rect width="360" height="225" rx="8" fill="url(#vanTone)" role="img" aria-label="Photo of the company's white delivery van"/>
  </svg>

  <p class="service-note">We proudly serve all of Southeast Missouri from our two locations:</p>

  <section class="location location--first">
    <h2>HARLOW RIDGE</h2>
    <p class="address">2140 W Linden Ave Ste 8</p>
    <p class="phones"><b>PH.</b> 555-210-4830<span class="gap"></span> <b>FAX.</b> 555-210-4831</p>
    <p class="landmark">(Across from Brightway Pharmacy and next door to Maple Bakery)</p>
  </section>

  <div class="divider"></div>

  <section class="location location--second">
    <h2>BRENTON</h2>
    <p class="address">415 S Cedar St</p>
    <p class="phones"><b>PH.</b> 555-318-6270<span class="gap"></span> <b>FAX.</b> 555-318-6271</p>
    <p class="landmark">(Between Heritage Bank and Fresh Market)</p>
  </section>
</main>
</body>
</html>
```